Equine Horse Employment site

We need to redesign the layout of Paddock Crew.co.uk

It will offer Job seekers and Employers the place to look for a job, and look for a candidate.

The logical format needs to be improved and the layout must look highly visually appealing.

It needs to be incredibly simple to use and one click access to any part of the site.

The homepage must convey the following

- Log in and register areas
- Current Job Listings
- Current CV's
- Exclusive Service Club button
- Search box to allow simple searching for Jobs or CVs

We need PSD layouts for Homepage, Job listing Page, CV listing Page, Job Profile and CV Profile. This job is for the design of 5 PSD screens.

Generic page for ancillary page such as about, contact and news.

The biggest competitor is StableandTack.com

Please ask us any questions and please be prepared to make changes, as we are very particular.

More work will be provided to the winning designer.

thanks

• It must not look cheap or like a job board, it has to have character and feel friendly, and inviting. Please do not submit poor designs that look like a job board, as they will be rejected instantly.

thanks

```html
<!DOCTYPE html>
<html lang="en">
<head>
<meta charset="utf-8">
<title>Paddock Crew — Equestrian Recruitment Specialists</title>
<link href="https://fonts.googleapis.com/css2?family=Arimo:wght@400;700&display=swap" rel="stylesheet">
<style>
:root{
  --dark:#403c3d;
  --dark-2:#2f2c2d;
  --red:#d9482f;
  --red-2:#c33d26;
  --blue:#5b95b9;
  --panel:#6a9fbf;
  --panel-line:#8ab6d0;
  --sky:#5aaee0;
  --text:#3a3a3a;
  --muted:#5c5c5c;
  --white:#fff;
  --navy:#1e3a52;
}
*{box-sizing:border-box;margin:0;padding:0}
html,body{width:1200px;height:1114px;overflow:hidden}
body{position:relative;background:var(--white);font-family:"Arimo",Arial,sans-serif;color:var(--text)}
.abs{position:absolute}
a{color:inherit;text-decoration:none}

/* top bar */
.topbar{left:0;top:0;width:1200px;height:33px;background:var(--dark)}
.tab{top:4px;height:29px;font-size:14px;font-weight:700;display:flex;align-items:center;justify-content:center;border-radius:3px 3px 0 0}
.tab--seekers{left:196px;width:110px;background:var(--white);color:#666}
.tab--employers{left:313px;width:105px;background:var(--red);color:var(--white)}
.post-prompt{left:733px;top:9px;font-size:14px;font-weight:700;color:var(--white)}
.btn{background:var(--red);color:var(--white);font-weight:700;display:flex;align-items:center;justify-content:center;border-radius:2px}
.btn--post{left:899px;top:4px;width:96px;height:25px;font-size:15px}

/* brand + login */
.brand{left:200px;top:76px;display:flex;align-items:center;gap:10px;font-size:24px;font-weight:400;color:var(--dark-2);letter-spacing:.5px}
.brand-dot{width:22px;height:22px;border-radius:50%;background:var(--red)}
.field{height:20px;border:1px solid #c8c8c8;background:#fff;font-size:10.5px;color:#8a8a8a;display:flex;align-items:center;padding-left:8px}
.btn--signin{left:851px;top:96px;width:62px;height:21px;background:var(--sky);font-size:12.5px}
.btn--register{left:919px;top:96px;width:73px;height:21px;font-size:12.5px}

/* nav */
.nav{left:200px;top:139px;width:793px;height:31px;background:linear-gradient(#3e3a3b,#2b2829);display:flex;border-radius:2px}
.nav a{color:var(--white);font-size:13px;display:flex;align-items:center;padding:0 18px;border-right:1px solid #555}
.nav a:last-child{border-right:none}

/* hero */
.hero{left:200px;top:177px;width:793px;height:142px;background:#3b3738;overflow:hidden}
.hero-photo{left:307px;top:0;width:486px;height:142px;background:linear-gradient(90deg,#3b3738 0%,#7a5a3f 25%,#9a7a5a 55%,#6b4a33 80%,#8b6c50 100%)}
.hero-title{left:37px;top:32px;color:var(--white);font-weight:700;line-height:1.1}
.hero-title .l1{display:block;font-size:37px}
.hero-title .l2{display:block;font-size:29px;margin-top:2px}

/* search */
.search{left:200px;top:319px;width:793px;height:44px;background:var(--dark-2);border-radius:0 0 3px 3px}
.search-label{left:59px;top:11px;font-size:18px;font-weight:700;color:var(--white)}
.select::after{content:"";position:absolute;right:0;top:0;width:20px;height:100%;border-left:1px solid #ccc}
.caret{position:absolute;right:6px;top:8px;width:0;height:0;border-left:4px solid transparent;border-right:4px solid transparent;border-top:5px solid #777;z-index:1}
.btn--search{left:664px;top:10px;width:114px;height:27px;font-size:15px}

/* featured jobs */
.section-title{font-size:18px;font-weight:700;color:var(--blue)}
.job{width:190px}
.job h3{font-size:14px;color:var(--blue);font-weight:700}
.job p{font-size:11px;line-height:14px;margin-top:6px;color:var(--text)}
.meta{display:flex;align-items:center;gap:4px;font-size:10.5px;color:var(--muted);margin-top:8px;white-space:nowrap}
.divider-v{width:1px;background:#ddd;top:404px;height:75px}
.arrow{width:28px;height:28px;border-radius:50%;background:var(--sky);top:414px;display:flex;align-items:center;justify-content:center;box-shadow:0 1px 2px rgba(0,0,0,.3)}
.shade{left:200px;top:504px;width:793px;height:6px;background:radial-gradient(ellipse at center,rgba(0,0,0,.08),transparent 70%)}

/* panels */
.panel{background:var(--panel);top:517px;height:346px;border-radius:2px}
.panel h2{position:absolute;font-size:18px;font-weight:700;color:var(--white)}
.latest-item{left:19px;width:176px;color:var(--white)}
.latest-item h3{font-size:14px;font-weight:700}
.latest-item p{font-size:10.5px;line-height:13.5px;margin-top:7px;color:#eef5fa}
.latest-item .meta{color:var(--white);margin-top:6px}
.rule{height:1px;background:var(--panel-line)}
.btn--alljobs{left:42px;top:305px;width:124px;height:28px;font-size:15px}

.staff{width:176px;color:var(--white)}
.avatar{width:48px;height:48px;background:#dfe6ee;border:2px solid #fff}
.staff-name{font-size:13.5px}
.staff-role{display:flex;justify-content:space-between;font-size:10.5px;font-weight:700;color:var(--navy);margin-top:3px}
.staff-bio{font-size:10.5px;line-height:13.5px;margin-top:1px}
.btn--seekers{left:720px;top:848px;width:183px;height:28px;font-size:15px}

/* footer */
.footer{left:0;top:891px;width:1200px;height:223px;background:var(--dark)}
.footer h2{font-size:17px;font-weight:700;color:var(--white)}
.footer h3{font-size:13.5px;font-weight:700;color:var(--white)}
.about p{font-size:10.6px;line-height:13.1px;color:var(--white);margin-top:8px}
.social{display:flex;gap:9px;margin-top:14px}
.social span{width:21px;height:21px;background:#d8d8d8;border-radius:2px}
.links ul{list-style:none;margin-top:9px}
.links li{font-size:10.6px;color:var(--white);height:18.6px}
.legal{left:0;top:1069px;width:1200px;border-top:1px solid #555;text-align:center;padding-top:13px;font-size:10.8px;color:var(--white)}
.legal a{color:#8cc0e3}
</style>
</head>
<body>

<header>
  <div class="abs topbar">
    <a class="abs tab tab--seekers" href="#">Job seekers</a>
    <a class="abs tab tab--employers" href="#">Employers</a>
    <span class="abs post-prompt">Looking to Post a job?</span>
    <a class="abs btn btn--post" href="#">Click here</a>
  </div>

  <div class="abs brand"><span class="brand-dot"></span>Paddock Crew</div>

  <div class="abs field" style="left:587px;top:97px;width:123px">User name</div>
  <div class="abs field" style="left:720px;top:97px;width:122px">Password</div>
  <a class="abs btn btn--signin" href="#">Sign in</a>
  <a class="abs btn btn--register" href="#">Register</a>

  <nav class="abs nav">
    <a href="#">Home</a><a href="#">About US</a><a href="#">Employers</a><a href="#">Advertise</a><a href="#">News</a><a href="#">Resources</a><a href="#">Helpful links</a>
  </nav>
</header>

<section class="abs hero">
  <div class="abs hero-photo" role="img" aria-label="Two chestnut horses looking out over stable doors"></div>
  <h1 class="abs hero-title"><span class="l1">Equestrian</span><span class="l2">Recruitment Specialists</span></h1>
</section>

<section class="abs search">
  <svg class="abs" style="left:21px;top:7px" width="30" height="30" viewBox="0 0 30 30"><circle cx="12" cy="12" r="9" fill="none" stroke="#8a8a8a" stroke-width="3"/><line x1="19" y1="19" x2="27" y2="27" stroke="#8a8a8a" stroke-width="4" stroke-linecap="round"/></svg>
  <span class="abs search-label">Search job</span>
  <div class="abs field" style="left:168px;top:11px;width:178px;height:24px">Enter job title</div>
  <div class="abs field select" style="left:358px;top:11px;width:148px;height:24px">Job type<span class="caret"></span></div>
  <div class="abs field select" style="left:518px;top:11px;width:131px;height:24px">Location<span class="caret"></span></div>
  <a class="abs btn btn--search" href="#">Search Jobs</a>
</section>

<section>
  <h2 class="abs section-title" style="left:201px;top:372px">FEATURED JOBS</h2>
  <a class="abs arrow" style="left:156px" href="#"><svg width="10" height="12" viewBox="0 0 10 12"><path d="M7 1 2 6l5 5" fill="none" stroke="#fff" stroke-width="2.5"/></svg></a>
  <a class="abs arrow" style="left:1002px" href="#"><svg width="10" height="12" viewBox="0 0 10 12"><path d="M3 1l5 5-5 5" fill="none" stroke="#fff" stroke-width="2.5"/></svg></a>

  <article class="abs job" style="left:204px;top:403px"><h3>Event Groom</h3><p>Full time event groom to join our team on a busy family event yard</p><div class="meta"><svg width="10" height="14" viewBox="0 0 10 14"><path d="M5 0a5 5 0 0 1 5 5c0 4-5 9-5 9S0 9 0 5a5 5 0 0 1 5-5z" fill="#e8694a"/><circle cx="5" cy="5" r="2" fill="#fff"/></svg>Where it is &nbsp;|&nbsp; Posted 14/05/2012</div></article>
  <div class="abs divider-v" style="left:391px"></div>
  <article class="abs job" style="left:409px;top:403px"><h3>Sales Exicutive</h3><p>Full time event groom to join our team on a busy family event yard</p><div class="meta"><svg width="10" height="14" viewBox="0 0 10 14"><path d="M5 0a5 5 0 0 1 5 5c0 4-5 9-5 9S0 9 0 5a5 5 0 0 1 5-5z" fill="#e8694a"/><circle cx="5" cy="5" r="2" fill="#fff"/></svg>Where it is &nbsp;|&nbsp; Posted 14/05/2012</div></article>
  <div class="abs divider-v" style="left:599px"></div>
  <article class="abs job" style="left:615px;top:403px;width:185px"><h3>Groom/Asistant Instructor</h3><p>Full time event groom to join our team on a busy family event yard</p><div class="meta"><svg width="10" height="14" viewBox="0 0 10 14"><path d="M5 0a5 5 0 0 1 5 5c0 4-5 9-5 9S0 9 0 5a5 5 0 0 1 5-5z" fill="#e8694a"/><circle cx="5" cy="5" r="2" fill="#fff"/></svg>Where it is &nbsp;|&nbsp; Posted 14/05/2012</div></article>
  <div class="abs divider-v" style="left:801px"></div>
  <article class="abs job" style="left:817px;top:403px"><h3>Instructor rider</h3><p>Full time event groom to join our team on a busy family event yard</p><div class="meta"><svg width="10" height="14" viewBox="0 0 10 14"><path d="M5 0a5 5 0 0 1 5 5c0 4-5 9-5 9S0 9 0 5a5 5 0 0 1 5-5z" fill="#e8694a"/><circle cx="5" cy="5" r="2" fill="#fff"/></svg>Where it is &nbsp;|&nbsp; Posted 14/05/2012</div></article>
  <div class="abs shade"></div>
</section>

<section class="abs panel" style="left:199px;width:211px">
  <h2 style="left:20px;top:14px">LATEST JOBS</h2>
  <article class="abs latest-item" style="top:47px"><h3>Event Groom</h3><p>Full time event groom to join our team on a busy family</p><div class="meta"><svg width="10" height="14" viewBox="0 0 10 14"><path d="M5 0a5 5 0 0 1 5 5c0 4-5 9-5 9S0 9 0 5a5 5 0 0 1 5-5z" fill="#fff"/><circle cx="5" cy="5" r="2" fill="#6a9fbf"/></svg>Where it is &nbsp;|&nbsp; Posted 14/05/2012</div></article>
  <div class="abs rule" style="left:15px;top:121px;width:180px"></div>
  <article class="abs latest-item" style="top:133px"><h3>Event Groom</h3><p>Full time event groom to join our team on a busy family</p><div class="meta"><svg width="10" height="14" viewBox="0 0 10 14"><path d="M5 0a5 5 0 0 1 5 5c0 4-5 9-5 9S0 9 0 5a5 5 0 0 1 5-5z" fill="#fff"/><circle cx="5" cy="5" r="2" fill="#6a9fbf"/></svg>Where it is &nbsp;|&nbsp; Posted 14/05/2012</div></article>
  <div class="abs rule" style="left:15px;top:207px;width:180px"></div>
  <article class="abs latest-item" style="top:219px"><h3>Event Groom</h3><p>Full time event groom to join our team on a busy family</p><div class="meta"><svg width="10" height="14" viewBox="0 0 10 14"><path d="M5 0a5 5 0 0 1 5 5c0 4-5 9-5 9S0 9 0 5a5 5 0 0 1 5-5z" fill="#fff"/><circle cx="5" cy="5" r="2" fill="#6a9fbf"/></svg>Where it is &nbsp;|&nbsp; Posted 14/05/2012</div></article>
  <div class="abs rule" style="left:15px;top:293px;width:180px"></div>
  <a class="abs btn btn--alljobs" href="#">View all jobs</a>
</section>

<section class="abs panel" style="left:418px;width:574px">
  <h2 style="left:16px;top:12px">FEATURED STAFF</h2>
</section>

<!-- staff grid -->
<div class="abs avatar" style="left:436px;top:569px" role="img" aria-label="Profile photo placeholder"></div>
<div class="abs staff" style="left:492px;top:567px"><div class="staff-name">Rowan Ellery</div><div class="staff-role"><span>Farm manager/trainer</span><span>25 Male</span></div><div class="staff-bio">grew up on training an breeding ranch. dad was a vet.</div></div>
<div class="abs avatar" style="left:695px;top:569px" role="img" aria-label="Profile photo placeholder"></div>
<div class="abs staff" style="left:758px;top:567px"><div class="staff-name">Rowan Ellery</div><div class="staff-role"><span>Farm manager/trainer</span><span>25 Male</span></div><div class="staff-bio">grew up on training an breeding ranch. dad was a vet.</div></div>
<div class="abs rule" style="left:492px;top:630px;width:176px"></div>
<div class="abs rule" style="left:758px;top:630px;width:176px"></div>

<div class="abs avatar" style="left:436px;top:638px" role="img" aria-label="Profile photo placeholder"></div>
<div class="abs staff" style="left:492px;top:636px"><div class="staff-name">Rowan Ellery</div><div class="staff-role"><span>Farm manager/trainer</span><span>25 Male</span></div><div class="staff-bio">grew up on training an breeding ranch. dad was a vet.</div></div>
<div class="abs avatar" style="left:695px;top:638px" role="img" aria-label="Profile photo placeholder"></div>
<div class="abs staff" style="left:758px;top:636px"><div class="staff-name">Rowan Ellery</div><div class="staff-role"><span>Farm manager/trainer</span><span>25 Male</span></div><div class="staff-bio">grew up on training an breeding ranch. dad was a vet.</div></div>
<div class="abs rule" style="left:492px;top:700px;width:176px"></div>
<div class="abs rule" style="left:758px;top:700px;width:176px"></div>

<div class="abs avatar" style="left:436px;top:707px" role="img" aria-label="Profile photo placeholder"></div>
<div class="abs staff" style="left:492px;top:705px"><div class="staff-name">Rowan Ellery</div><div class="staff-role"><span>Farm manager/trainer</span><span>25 Male</span></div><div class="staff-bio">grew up on training an breeding ranch. dad was a vet.</div></div>
<div class="abs avatar" style="left:695px;top:707px" role="img" aria-label="Profile photo placeholder"></div>
<div class="abs staff" style="left:758px;top:705px"><div class="staff-name">Rowan Ellery</div><div class="staff-role"><span>Farm manager/trainer</span><span>25 Male</span></div><div class="staff-bio">grew up on training an breeding ranch. dad was a vet.</div></div>
<div class="abs rule" style="left:492px;top:769px;width:176px"></div>
<div class="abs rule" style="left:758px;top:769px;width:176px"></div>

<div class="abs avatar" style="left:436px;top:779px" role="img" aria-label="Profile photo placeholder"></div>
<div class="abs staff" style="left:492px;top:777px"><div class="staff-name">Rowan Ellery</div><div class="staff-role"><span>Farm manager/trainer</span><span>25 Male</span></div><div class="staff-bio">grew up on training an breeding ranch. dad was a vet.</div></div>
<div class="abs avatar" style="left:695px;top:779px" role="img" aria-label="Profile photo placeholder"></div>
<div class="abs staff" style="left:758px;top:777px"><div class="staff-name">Rowan Ellery</div><div class="staff-role"><span>Farm manager/trainer</span><span>25 Male</span></div><div class="staff-bio">grew up on training an breeding ranch. dad was a vet.</div></div>

<a class="abs btn btn--seekers" href="#">View all job seekers</a>

<footer class="abs footer">
  <div class="abs about" style="left:200px;top:12px;width:335px">
    <h2>About Paddock Crew</h2>
    <p>Lorem Ipsum is simply dummy text of the printing and typesetting industry. Lorem Ipsum has been the industry's standard dummy text ever since the 1500s, when an unknown printer took a galley of type and scrambled it to make a type specimen book. It has survived not only five centuries, but also the leap into electronic typesetting, remaining essentially unchanged.</p>
    <div class="social"><span></span><span></span><span></span><span></span></div>
  </div>
  <div class="abs links" style="left:588px;top:22px"><h3>Employers</h3><ul><li>What you get</li><li>How we work</li><li>Register</li><li>Login</li><li>Groom Search</li><li>FAQs</li></ul></div>
  <div class="abs links" style="left:700px;top:22px"><h3>Grooms</h3><ul><li>What you get</li><li>How we work</li><li>Register CV</li><li>Login</li><li>Job Search</li><li>FAQs</li></ul></div>
  <div class="abs links" style="left:803px;top:22px"><h3>Featured jobs</h3><ul><li>Head Groom</li><li>Stallion Hander - Australia</li><li>Instructor rider</li><li>Riding Instructor</li><li>Polo Groom</li><li>secretary/admin/telesales</li></ul></div>
</footer>
<div class="abs legal">Copyright Paddock Crew 2012. Use of this website constitutes acceptance of our <a href="#">User Agreement and Privacy Policy</a></div>

</body>
</html>
```